One page company profile for exclusive wine import

Valtrenor is an importer of exclusive, rare wines into indonesia. We would like a stylish, classy, upmarket but professional one pager containing our company profile.

Please include the text we prepared (see must haves) and read through it to get a better understanding of what our company is doing

We would like the one pager to have a dark background, and contain a drawing or drawing-style picture related to wine and/or global import (see examples). We would like to have it in PDF as well as in a word-template so we can later produce translations and/or adaptations to the text.

Target Market(s)

The one pagers is directed to distributors and upmarket hotels and restaurants.

Requirements
Must have
• We would like the one pager to have a dark background, and contain a drawing or drawing-style picture related to wine and/or global import (see examples)
• Our logo (see files) on the one pager
• The following contact details: E-mail: info@valtrenor-example.eu
• Word template and PDF
• The following text:
• "Valtrenor brings rare, exceptional wines to the Indonesian market. We
• specialize in French and Italian wines that even in Europe are very hard
• to get by. We have an extensive network of big and small, famous and less
• known winemakers that reserve a portion of their production for us.
• Together with them, we supply the market with an excellent range of the
• absolute best European wines.
• We buy our products directly at the winemaker in France or Italy Through a
• licensed importer, the wines are brought to Indonesia by airfreight and
• stored in air-conditioned, optimal conditions, awaiting distribution to
• our customers. All of this ensured that the wine loses none of its quality
• during transport from the winemaker to the customer.
• We always look out for partners that are eager to distribute or retail.
• Our intentions working with them are always to work on a long term basis.
• With these intentions we see that both sides together have to engage
• themselves to succeed in sales and establishing brand recognition in the
• Indonesian market. Our philosophy is based on trust, responsibility,
• mutual respect and of course a love for great wine!
• We advise our clients on tasting, food pairing, storing and aging the wine
• and provide a technical datasheet with all our bottles. We pride ourselves
• in our customer service and are always available for any enquiry."
Should not have
• clichés like pictures of grapes, vineyards, barrels, etc... (stylised drawings are preferred and allowed)

```html
<!DOCTYPE html>
<html lang="en">
<head>
<meta charset="utf-8">
<title>Valtrenor — Company Profile</title>
<link rel="stylesheet" href="https://fonts.googleapis.com/css2?family=Cinzel:wght@400;600&family=Cardo&family=Open+Sans:ital,wght@0,400;0,700;1,400;1,700&display=swap">
<style>
  :root {
    --backdrop: #dcdcdc;
    --sheet: #0b0b0b;
    --gold: #d9a93a;
    --ink-light: #e6e2da;
    --paper: #d3d1ce;
    --ink-dark: #1b1b1b;
    --brand-navy: #1f3a78;
    --map-tone: #2a2a2a;
    --splash: #b9a58c;
  }
  * { box-sizing: border-box; margin: 0; padding: 0; }
  html, body { width: 1200px; height: 1200px; overflow: hidden; background: var(--backdrop); }
  .flyer {
    position: absolute; left: 190px; top: 20px;
    width: 820px; height: 1160px;
    background: var(--sheet); overflow: hidden;
    box-shadow: 0 6px 24px rgba(0,0,0,.25);
  }
  .world-map {
    position: absolute; left: 300px; top: 40px; width: 520px; height: 460px;
    background: radial-gradient(ellipse at 55% 45%, var(--map-tone), rgba(11,11,11,0) 70%);
  }
  .bottle-art {
    position: absolute; left: 0; top: 0; width: 470px; height: 800px;
    background:
      radial-gradient(ellipse at 55% 40%, rgba(230,224,205,.85) 0 18%, rgba(185,165,140,.55) 32%, rgba(11,11,11,0) 62%),
      linear-gradient(180deg, #1a1a1a, #0b0b0b);
  }
  .profile-text {
    position: absolute; left: 440px; top: 150px; width: 350px;
    font-family: "Cardo", Georgia, serif; color: var(--ink-light);
  }
  .headline {
    font-family: "Cinzel", "Times New Roman", serif; font-weight: 400;
    font-size: 31px; line-height: 1.12; letter-spacing: .06em;
    color: var(--ink-light); margin-bottom: 30px;
  }
  .headline .accent { color: var(--gold); }
  .profile-text p { font-size: 15px; line-height: 1.45; margin-bottom: 16px; }
  .profile-text p::first-letter { color: var(--gold); font-size: 22px; }
  .torn-paper { position: absolute; left: 0; top: 740px; width: 820px; height: 420px; }
  .closing {
    position: absolute; left: 110px; top: 800px; width: 600px;
    text-align: center; font-family: "Open Sans", Arial, sans-serif; color: var(--ink-dark);
  }
  .brand {
    display: inline-flex; align-items: center; gap: 10px; margin-bottom: 18px;
    font-family: "Open Sans", Arial, sans-serif; font-weight: 700; font-size: 30px;
    letter-spacing: .06em; color: var(--brand-navy); text-transform: uppercase;
  }
  .brand-dot { width: 30px; height: 30px; border-radius: 50%; background: var(--brand-navy); }
  .closing p { font-size: 14px; line-height: 1.5; font-style: italic; margin-bottom: 16px; }
  .closing .service { font-weight: 700; }
  .contact { font-size: 20px; letter-spacing: .08em; margin-top: 6px; }
</style>
</head>
<body>
  <main class="flyer">
    <div class="world-map" role="img" aria-label="Faint world map showing Europe and Indonesia"></div>
    <div class="bottle-art" role="img" aria-label="Stylised drawing of a white wine bottle with a splash of wine behind it"></div>

    <section class="profile-text">
      <h1 class="headline"><span class="accent">Valtrenor brings rare, exceptional wines</span> to the Indonesian market.</h1>
      <p>We specialize in French and Italian wines that even in Europe are very hard to get by.</p>
      <p>We have an extensive network of big and small, famous and less known winemakers that reserve a portion of their production for us.</p>
      <p>Together with them, we supply the market with an excellent range of the absolute best European wines.</p>
      <p>We buy our products directly at the winemaker in France or Italy. Through a licensed importer, the wines are brought to Indonesia by airfreight and stored in air-conditioned, optimal conditions, awaiting distribution to our customers.</p>
    </section>

    <svg class="torn-paper" viewBox="0 0 820 420" aria-hidden="true">
      <polygon fill="var(--paper)" points="60,40 120,22 170,34 230,12 300,28 360,8 420,30 470,14 540,36 600,18 660,40 720,26 760,48 770,110 752,160 774,220 756,280 770,340 740,380 680,392 620,378 560,398 500,384 440,400 380,386 320,402 260,388 200,400 140,382 90,394 60,360 74,300 52,240 70,180 48,120 66,80"/>
    </svg>

    <section class="closing">
      <div class="brand"><span class="brand-dot"></span>Valtrenor</div>
      <p>All of this ensured that the wine loses none of its quality during transport from the winemaker to the customer. We always look out for partners that are eager to distribute or retail. Our intentions working with them are always to work on a long term basis. With these intentions we see that both sides together have to engage themselves to succeed in sales and establishing brand recognition in the Indonesian market. Our philosophy is based on trust, responsibility, mutual respect and of course a love for great wine!</p>
      <p class="service">We advise our clients on tasting, food pairing, storing and aging the wine and provide a technical datasheet with all our bottles. We pride ourselves in our customer service and are always available for any enquiry.</p>
      <div class="contact">info@valtrenor-example.eu</div>
    </section>
  </main>
</body>
</html>
```